Sleek, Professional Business Card Design Needed

Business Cards - Logo Attached.

We are a solar consulting company. We are national and want our cards to represent the professional high quality products that we offer.

Industry/Entity Type

Business

Contact Information for Business Card

n/a

Requirements
Must have
• Design
• Name
• Position
• Number
• Email
• Address
Should not have
• Not be too crowded

```html
<!DOCTYPE html>
<html lang="en">
<head>
<meta charset="utf-8">
<title>Sunline Advisory – Business Card</title>
<link href="https://fonts.googleapis.com/css2?family=Montserrat:wght@400;500;600&display=swap" rel="stylesheet">
<style>
  :root {
    --blue: #0f8fcc;
    --white: #ffffff;
    --paper: #f1f1f1;
    --green: #8cc63f;
    --ink: #0f7fc0;
    --bg: #2b2b2b;
  }
  * { box-sizing: border-box; margin: 0; padding: 0; }
  html, body { width: 1200px; height: 749px; overflow: hidden; background: var(--bg); }
  body { font-family: "Montserrat", sans-serif; position: relative; }

  .card {
    position: absolute; top: 226px;
    width: 520px; height: 297px;
    border-radius: 22px; overflow: hidden;
    background: var(--blue);
  }
  .card--front { left: 50px; }
  .card--back { left: 630px; }

  /* front */
  .front__brand {
    position: absolute; left: 0; right: 0; top: 0; height: 196px;
    display: flex; flex-direction: column; align-items: center; justify-content: center; gap: 14px;
  }
  .brand__mark {
    width: 64px; height: 64px; border-radius: 50%;
    border: 6px solid var(--white);
  }
  .brand__name {
    color: var(--white); font-weight: 500; font-size: 30px; letter-spacing: 2px;
    padding-bottom: 8px; border-bottom: 1.5px solid var(--white);
  }
  .front__band {
    position: absolute; left: 0; right: 0; top: 196px; height: 86px;
    background: var(--white);
  }
  .front__web {
    position: absolute; left: 0; right: 0; top: 14px; text-align: center;
    color: var(--ink); font-size: 15px; font-weight: 500; letter-spacing: .5px;
  }
  .front__accent {
    position: absolute; left: 222px; width: 112px; top: 188px; height: 8px;
    background: var(--green);
  }

  /* back */
  .back__grid {
    position: absolute; left: 10px; right: 10px; top: 10px; height: 200px;
    display: grid; grid-template-columns: repeat(3, 1fr); grid-template-rows: 1fr 1fr;
    border: 1px solid rgba(255,255,255,.6);
  }
  .tile { display: flex; align-items: center; justify-content: center; text-align: center; }
  .tile--info {
    background: radial-gradient(circle, var(--white) 40%, #e4e4e4 100%);
    color: var(--ink); font-size: 12px; line-height: 1.45; font-weight: 500;
  }
  .tile--icon { background: var(--blue); }
  .icon { width: 54px; height: 54px; }
  .back__band {
    position: absolute; left: 0; right: 0; top: 214px; height: 68px;
    background: var(--white);
    display: flex; align-items: center; justify-content: center; gap: 12px;
  }
  .person__name { color: var(--ink); font-size: 22px; font-weight: 600; letter-spacing: 1px; }
  .person__role {
    color: var(--green); font-size: 11px; font-weight: 500; letter-spacing: 1px;
    border: 1.5px solid var(--ink); padding: 3px 8px;
  }
  .back__accent {
    position: absolute; left: 250px; width: 110px; top: 274px; height: 8px;
    background: var(--green);
  }
</style>
</head>
<body>

<section class="card card--front" aria-label="Card front">
  <div class="front__brand">
    <div class="brand__mark"></div>
    <div class="brand__name">SUNLINE ADVISORY</div>
  </div>
  <div class="front__accent"></div>
  <div class="front__band">
    <p class="front__web">www.sunlineadvisory.com</p>
  </div>
</section>

<section class="card card--back" aria-label="Card back">
  <div class="back__grid">
    <div class="tile tile--info"><p>48 Linden Street<br>Brookfield 20417</p></div>
    <div class="tile tile--icon">
      <svg class="icon" viewBox="0 0 54 54" aria-label="Phone">
        <circle cx="27" cy="27" r="24" fill="none" stroke="#fff" stroke-width="2.5"/>
        <path d="M20 18c2-1 3 0 4 3l-1 2c1 3 3 5 6 6l2-1c3 1 4 2 3 4l-2 2c-7 0-14-7-14-14z" fill="#fff"/>
      </svg>
    </div>
    <div class="tile tile--info"><p>mara.ellis@mail.com<br>www.maraellis.com</p></div>
    <div class="tile tile--icon">
      <svg class="icon" viewBox="0 0 54 54" aria-label="Location">
        <circle cx="27" cy="27" r="24" fill="none" stroke="#fff" stroke-width="2.5"/>
        <path d="M27 38c-5-6-8-10-8-14a8 8 0 0 1 16 0c0 4-3 8-8 14z" fill="#fff"/>
        <circle cx="27" cy="24" r="3" fill="var(--blue)"/>
      </svg>
    </div>
    <div class="tile tile--info"><p>000 - 2417 - 3380<br>000 - 2417 - 3381</p></div>
    <div class="tile tile--icon">
      <svg class="icon" viewBox="0 0 54 54" aria-label="Website">
        <circle cx="27" cy="27" r="24" fill="none" stroke="#fff" stroke-width="2.5"/>
        <rect x="17" y="18" width="20" height="14" fill="none" stroke="#fff" stroke-width="2.5"/>
        <path d="M23 37h8M27 32v5" stroke="#fff" stroke-width="2.5"/>
      </svg>
    </div>
  </div>
  <div class="back__band">
    <span class="person__name">MARA ELLIS</span>
    <span class="person__role">ACCOUNTANT</span>
  </div>
  <div class="back__accent"></div>
</section>

</body>
</html>
```